Website redesign for Tawny Reef Advisory

www.tawnyreefadvisory.example

We need to redesign our not-yet-designed website. It has the basic features and most of the functionality we want, but something isn't coming together with the design and we thought we'd stop trying to get the template to do what we want it to do and let a professional design it. :)

Our key focus is digital marketing: SEO, PPC, Social Media and Local Directories. We also do web development and marketing strategy.

Websites I like:
www.coldharborstudio.example
www.lowtidewire.example
www.hikeowlonline.example

Target Market(s)

Small businesses

Industry/Entity Type

Marketing

Contact Information for Business Card

Logo, Name, Phone, email, Web, Twitter, Logo and tag on the back

Coding

Coded - Design and coding required

Number of Pages Required

2 page

Font styles to use
Serif
Sans Serif

Requirements
Must have
• Besides the information that is currently on the website, it will have two conversion areas. One conversion is for the Ratekit.io reputation management widget and the other is for an SEO site audit widget from Dunefold.example
• Only one widget is on the current website, the other needs to be added.
Nice to have
• I'd like the website to flow better than it does and have more cohesiveness. We can keep the video in the banner but it's way too big as it is, so if we do keep it we'd have to size it down considerably.
Should not have
• Can't think of anything for here but if I do, i'll add it later.

```html
<!DOCTYPE html>
<html lang="en">
<head>
<meta charset="utf-8">
<title>Tawny Reef Advisory</title>
<link href="https://fonts.googleapis.com/css2?family=Roboto:wght@300;400;500;700&family=Roboto+Condensed:wght@400;700&display=swap" rel="stylesheet">
<style>
:root{
  --red:#c5323a;
  --red-dark:#a8262e;
  --ink:#2b2b2b;
  --text:#5a5a5a;
  --muted:#8a8a8a;
  --light:#f1f1f1;
  --dark:#2e2e2e;
  --slate:#3f4b55;
  --night:#262626;
  --black:#141414;
  --white:#ffffff;
}
*{box-sizing:border-box;margin:0;padding:0}
html,body{width:1200px;height:3797px;overflow:hidden}
body{font-family:"Roboto",Arial,sans-serif;color:var(--text);background:var(--white);font-size:13px;line-height:1.55}
.head{font-family:"Roboto Condensed","Arial Narrow",sans-serif;font-weight:400;text-transform:uppercase;color:var(--ink)}
section{position:relative;width:1200px;overflow:hidden}

/* hero */
.hero{height:663px}
.hero-photo{position:absolute;inset:0;background:linear-gradient(135deg,#8d6f52 0%,#b39373 30%,#c7ab8a 55%,#9b7b5c 80%,#6f5640 100%)}
.hero-shade{position:absolute;inset:0;background:rgba(30,20,12,.28)}
.brand{position:absolute;left:114px;top:40px;display:flex;flex-direction:column;align-items:center;gap:10px;width:130px}
.brand-dot{width:92px;height:92px;border-radius:50%;background:var(--red)}
.brand-name{color:var(--white);font-family:"Roboto Condensed",sans-serif;font-weight:700;font-size:19px;line-height:1.1;text-align:center;text-transform:uppercase}
.nav{position:absolute;right:96px;top:48px;display:flex;gap:34px}
.nav a{color:var(--white);text-decoration:none;font-size:14px;font-weight:500;letter-spacing:.3px;padding-bottom:6px}
.nav a.active{border-bottom:2px solid var(--red)}
.arrow{position:absolute;top:228px;width:30px;height:30px;border-radius:50%;background:rgba(255,255,255,.55);display:flex;align-items:center;justify-content:center}
.arrow.left{left:56px}.arrow.right{right:56px}
.hero-copy{position:absolute;left:0;right:0;top:318px;text-align:center;color:var(--white)}
.hero-copy .kicker{font-size:28px;font-weight:500;font-family:"Roboto Condensed",sans-serif}
.hero-copy h1{font-family:"Roboto Condensed",sans-serif;font-weight:700;font-size:58px;line-height:1.1;margin-top:4px}
.hero-copy .sub{font-size:21px;font-weight:700;font-family:"Roboto Condensed",sans-serif;margin-top:4px}

/* about */
.about{height:730px;background:var(--white)}
.about-media{position:absolute;left:109px;top:66px;width:372px;height:310px;background:linear-gradient(160deg,#5d6d7e,#25303b 60%,#cfd4d9 61%,#e6e8ea)}
.about-copy{position:absolute;left:560px;top:62px;width:540px}
.title-row{display:flex;align-items:center;gap:14px}
.title-dot{width:48px;height:48px;border-radius:50%;background:var(--red);flex:none}
.about-copy h2{font-size:29px;line-height:1}
.about-copy .tag{font-size:14px;color:var(--text);margin-top:4px}
.about-copy p{font-size:11.5px;margin-top:16px;margin-left:2px;line-height:1.65}
.features{position:absolute;left:96px;top:448px;width:1008px;display:grid;grid-template-columns:repeat(4,1fr);gap:44px}
.feature .ico{width:62px;height:58px;background:var(--red);display:flex;align-items:center;justify-content:center}
.feature h3{font-family:"Roboto",sans-serif;font-weight:400;font-size:19px;color:var(--ink);margin-top:24px}
.feature p{font-size:11.5px;margin-top:12px;height:56px;overflow:hidden}
.more{font-size:11px;color:var(--ink);text-transform:uppercase;margin-top:12px;display:flex;align-items:center;gap:6px}

/* reputation */
.reputation{height:400px;background:var(--light)}
.rep-top{position:relative;z-index:2;text-align:center;padding-top:52px}
.rep-top h2{font-size:29px;line-height:1.2;color:var(--ink)}
.rep-band{position:absolute;left:0;right:0;top:92px;height:308px;background:var(--dark);clip-path:polygon(0 30px,100% 0,100% 100%,0 100%)}
.cta{position:absolute;top:134px;display:flex;gap:30px;color:var(--white)}
.cta.one{left:96px}.cta.two{left:660px}
.cta .box{width:100px;height:100px;background:var(--white);display:flex;align-items:center;justify-content:center;flex:none}
.cta h3{font-family:"Roboto",sans-serif;font-weight:500;font-size:16px;line-height:1.35;text-transform:uppercase}
.btn{display:inline-block;background:var(--red);color:var(--white);font-size:13px;font-weight:500;text-transform:uppercase;padding:9px 20px;margin-top:14px}

/* services */
.services{height:612px;background:var(--white);text-align:center}
.services h2{font-size:31px;padding-top:62px}
.services .lead{width:920px;margin:10px auto 0;font-size:11.5px}
.svc-grid{position:absolute;left:96px;top:212px;width:1008px;display:grid;grid-template-columns:repeat(3,1fr);row-gap:48px;text-align:left}
.svc{display:flex;gap:20px}
.svc .circle{width:82px;height:82px;border-radius:50%;background:var(--red);flex:none;display:flex;align-items:center;justify-content:center}
.svc h3{font-family:"Roboto",sans-serif;font-weight:400;font-size:17px;color:var(--ink)}
.svc p{font-size:11px;margin-top:8px;width:200px;height:52px;overflow:hidden}
.svc .read{font-size:12px;color:var(--muted);margin-top:14px}

/* plans */
.plans{height:603px;background:var(--light);text-align:center}
.plans h2{font-size:31px;padding-top:48px}
.plans .lead{font-size:15px;margin-top:2px}
.plan-grid{position:absolute;left:96px;top:211px;width:1008px;display:grid;grid-template-columns:repeat(3,314px);justify-content:space-between}
.plan{background:var(--white);border:1px solid #e2a4a7;height:321px;position:relative;padding-top:128px;text-align:left}
.plan .badge{position:absolute;left:50%;top:-26px;transform:translateX(-50%);width:124px;height:124px;border-radius:50%;background:var(--white);border:4px solid var(--red);display:flex;align-items:center;justify-content:center}
.plan h3{font-family:"Roboto",sans-serif;font-weight:500;color:var(--red);font-size:13px;text-transform:uppercase;text-align:center}
.plan ul{list-style:none;margin:24px 0 0 30px}
.plan li{font-size:11.5px;color:var(--ink);margin-bottom:14px;display:flex;align-items:center;gap:12px}
.plan li:before{content:"";width:5px;height:5px;border-top:1.5px solid var(--red);border-right:1.5px solid var(--red);transform:rotate(45deg)}

/* audit */
.audit{height:258px;background:var(--slate);text-align:center;color:var(--white)}
.audit h2{color:var(--white);font-size:34px;padding-top:56px}
.audit p{width:980px;margin:8px auto 0;font-size:12px;line-height:1.6}
.audit-widget{display:inline-flex;align-items:center;gap:10px;margin-top:18px}
.audit-widget .sq{width:22px;height:22px;background:#f1a23a}
.audit-widget span{font-size:26px;font-weight:700;color:#f1a23a}

/* contact */
.contact{height:456px;background:var(--night);color:var(--white)}
.contact h2{color:var(--white);font-size:31px;text-align:center;padding-top:58px}
.contact .lead{width:640px;margin:14px auto 0;text-align:center;font-size:13px;line-height:1.6}
.form{position:absolute;left:99px;top:198px;width:276px}
.field{height:38px;border:1px solid #bfbfbf;margin-bottom:16px;font-size:11px;padding:10px 12px;color:#d8d8d8}
.submit{height:36px;background:var(--red);color:var(--white);font-size:13px;font-weight:700;text-transform:uppercase;padding:9px 36px}
.message{position:absolute;left:389px;top:198px;width:384px;height:194px;border:1px solid #bfbfbf;font-size:11px;padding:10px 12px;color:#d8d8d8}
.info{position:absolute;left:812px;top:212px;width:300px}
.info-top{display:flex;gap:18px;align-items:flex-start}
.info-dot{width:74px;height:74px;border-radius:50%;background:var(--red);flex:none}
.info-top p{font-size:12px;line-height:1.45;margin-top:6px}
.info-line{display:flex;align-items:center;gap:12px;font-size:14px;margin-top:20px}
.info-line:first-of-type{margin-top:26px}

/* footer */
.footer{height:75px;background:var(--black);color:#cfcfcf;font-size:11px;display:flex;align-items:center;justify-content:space-between;padding:0 96px}
.social{display:flex;align-items:center;gap:10px}
.social i{width:26px;height:26px;border-radius:50%;background:var(--white);display:block}
</style>
</head>
<body>

<section class="hero">
  <div class="hero-photo" role="img" aria-label="Overhead photo of a work desk with laptop, notebooks, phone, coffee and glasses"></div>
  <div class="hero-shade"></div>
  <div class="brand">
    <div class="brand-dot"></div>
    <div class="brand-name">Tawny Reef Advisory</div>
  </div>
  <nav class="nav">
    <a>HOME</a><a class="active">ABOUT US</a><a>SERVICES</a><a>TEAM</a><a>BLOG</a><a>CONTACT US</a>
  </nav>
  <div class="arrow left"><svg width="12" height="12" viewBox="0 0 12 12"><path d="M8 1L3 6l5 5" stroke="#333" stroke-width="2" fill="none"/></svg></div>
  <div class="arrow right"><svg width="12" height="12" viewBox="0 0 12 12"><path d="M4 1l5 5-5 5" stroke="#333" stroke-width="2" fill="none"/></svg></div>
  <div class="hero-copy">
    <div class="kicker">HELLO THERE</div>
    <h1>WE ARE TAWNY REEF</h1>
    <div class="sub">WE HELP YOUR BUSINESS WIN THE INTERNET</div>
  </div>
</section>

<section class="about">
  <div class="about-media" role="img" aria-label="Desktop monitor showing a businessman beside a rising growth chart"></div>
  <div class="about-copy">
    <div class="title-row">
      <div class="title-dot"></div>
      <div>
        <h2 class="head">Big Results For Your Business</h2>
        <div class="tag">Expert &amp; Affordable Digital Marketing Services</div>
      </div>
    </div>
    <p>Tawny Reef's digital marketing services provide big results at affordable prices, making us a perfect fit for businesses of all types who need a bigger online footprint in order to grow. We create custom digital marketing strategies for businesses of all sizes, from web design and search engine optimization (SEO) to pay-per-click (PPC) campaigns and search engine reputation management (SERM). We work with you, step by step, to develop, implement, and monitor a digital marketing plan specifically tailored to the unique needs of your business.</p>
    <p>Tawny Reef is not our first time at the digital marketing rodeo. We've built our expertise providing local SEO and online reputation management services to businesses for over 10 years, and we're ready to put our experience to work for you. Our services leverage your digital marketing investment so you can run with the big dogs online - at a fraction of the cost of a big dog advertising budget.</p>
  </div>
  <div class="features">
    <div class="feature">
      <div class="ico"><svg width="28" height="28" viewBox="0 0 28 28" fill="#fff"><path d="M14 2L2 8v3h24V8z"/><rect x="5" y="12" width="3" height="10"/><rect x="12.5" y="12" width="3" height="10"/><rect x="20" y="12" width="3" height="10"/><rect x="2" y="23" width="24" height="3"/></svg></div>
      <h3>Build Your Brand</h3>
      <p>Tawny Reef will help you zero in on your business' unique value proposition - what sets you apart and makes you memorable.</p>
      <div class="more">Click here <svg width="9" height="9" viewBox="0 0 10 10"><circle cx="5" cy="5" r="5" fill="#2b2b2b"/><path d="M4 3l2 2-2 2" stroke="#fff" fill="none"/></svg></div>
    </div>
    <div class="feature">
      <div class="ico"><svg width="28" height="28" viewBox="0 0 28 28"><circle cx="14" cy="14" r="11" fill="#fff"/><path d="M9 9c3 1 4 3 3 6s2 4 4 6M17 5c-1 3 2 4 4 4" stroke="#c5323a" stroke-width="2" fill="none"/></svg></div>
      <h3>Build Your Website</h3>
      <p>We'll design a state-of-the-art website to wow your visitors. Your website is increasingly becoming the place where most buyers start.</p>
      <div class="more">Click here <svg width="9" height="9" viewBox="0 0 10 10"><circle cx="5" cy="5" r="5" fill="#2b2b2b"/><path d="M4 3l2 2-2 2" stroke="#fff" fill="none"/></svg></div>
    </div>
    <div class="feature">
      <div class="ico"><svg width="28" height="28" viewBox="0 0 28 28" fill="#fff"><circle cx="14" cy="9" r="5"/><path d="M5 25c0-6 4-10 9-10s9 4 9 10z"/></svg></div>
      <h3>Position Your Brand</h3>
      <p>We'll position your business online to capture higher search rankings with sound, up-to-date SEO practices and tactics.</p>
      <div class="more">Click here <svg width="9" height="9" viewBox="0 0 10 10"><circle cx="5" cy="5" r="5" fill="#2b2b2b"/><path d="M4 3l2 2-2 2" stroke="#fff" fill="none"/></svg></div>
    </div>
    <div class="feature">
      <div class="ico"><svg width="28" height="28" viewBox="0 0 28 28" fill="none" stroke="#fff" stroke-width="2.5"><path d="M3 3v22h22"/><path d="M7 19l6-7 4 4 7-9"/></svg></div>
      <h3>Build Your Reputation</h3>
      <p>Tawny Reef can help you turn customers into reviewers - crucial for boosting your search ranking and converting visitors.</p>
      <div class="more">Click here <svg width="9" height="9" viewBox="0 0 10 10"><circle cx="5" cy="5" r="5" fill="#2b2b2b"/><path d="M4 3l2 2-2 2" stroke="#fff" fill="none"/></svg></div>
    </div>
  </div>
</section>

<section class="reputation">
  <div class="rep-top"><h2 class="head">Reputation Management</h2></div>
  <div class="rep-band">
    <div class="cta one">
      <div class="box"><svg width="50" height="50" viewBox="0 0 50 50" fill="#c5323a"><path d="M4 24L46 6 36 44 24 30z"/><path d="M24 30l-2 12 6-8z" fill="#a8262e"/></svg></div>
      <div>
        <h3>Get a free report on your business'<br>online reviews.</h3>
        <span class="btn">Check my reviews</span>
      </div>
    </div>
    <div class="cta two">
      <div class="box"><svg width="50" height="40" viewBox="0 0 50 40" fill="none" stroke="#c5323a" stroke-width="3"><rect x="3" y="4" width="44" height="32"/><path d="M3 4l22 18L47 4"/></svg></div>
      <div>
        <h3>Ready to start generating reviews<br>for your business?</h3>
        <span class="btn" style="padding:9px 36px">Sign up now</span>
      </div>
    </div>
  </div>
</section>

<section class="services">
  <h2 class="head">Digital Marketing Services</h2>
  <p class="lead">Tawny Reef's digital marketing services are the cards you need for an internet-winning hand. Choose one or a combination of several services for a stronger hand, or choose them all for a hand that's unbeatable. Any of our digital marketing services will help you build your online profile - but all of them working together deliver big results.</p>
  <div class="svc-grid">
    <div class="svc">
      <div class="circle"><svg width="36" height="36" viewBox="0 0 36 36" fill="none" stroke="#fff" stroke-width="3.5"><circle cx="15" cy="15" r="9"/><path d="M22 22l9 9"/></svg></div>
      <div><h3>Search Engine Optimization</h3><p>SEO determines whether your business website will be seen by your target customers or not, and Seekly's rules keep changing.</p><div class="read">Read More &rsaquo;</div></div>
    </div>
    <div class="svc">
      <div class="circle"><svg width="36" height="36" viewBox="0 0 36 36" fill="#fff"><path d="M30 6c-8 0-14 5-17 12l5 5c7-3 12-9 12-17z"/><path d="M12 17l-6 1-3 5 7-1zM19 24l-1 6-5 3 1-7z"/><circle cx="23" cy="13" r="2.5" fill="#c5323a"/></svg></div>
      <div><h3>Reputation Management</h3><p>Word-of-mouth has always been the most powerful and effective marketing tool, and it's just as true online today.</p><div class="read">Read More &rsaquo;</div></div>
    </div>
    <div class="svc">
      <div class="circle"><svg width="36" height="36" viewBox="0 0 36 36" fill="#fff"><path d="M4 14h7l14-8v24l-14-8H4z"/><path d="M9 22l3 8h4l-3-8z"/><path d="M29 12l4-3M29 18h5M29 24l4 3" stroke="#fff" stroke-width="2"/></svg></div>
      <div><h3>Pay-Per-Click Advertising</h3><p>Boost your site to the front of the pack with Tawny Reef's pay-per-click advertising services. We zero in on buyers.</p><div class="read">Read More &rsaquo;</div></div>
    </div>
    <div class="svc">
      <div class="circle"><svg width="36" height="36" viewBox="0 0 36 36" fill="none" stroke="#fff" stroke-width="3"><rect x="4" y="6" width="28" height="19"/><path d="M12 31h12M18 25v6"/></svg></div>
      <div><h3>Website Development</h3><p>These days, if your business doesn't have a website, most potential customers will never know you exist at all.</p><div class="read">Read More &rsaquo;</div></div>
    </div>
    <div class="svc">
      <div class="circle"><svg width="36" height="36" viewBox="0 0 36 36"><circle cx="18" cy="18" r="13" fill="#fff"/><path d="M11 11c4 1 5 4 4 7s2 5 5 7M21 6c-1 4 3 5 6 5" stroke="#c5323a" stroke-width="2.5" fill="none"/></svg></div>
      <div><h3>Social Media Marketing</h3><p>Social media platforms like Friendhub aren't just great ways to engage with existing and potential customers.</p><div class="read">Read More &rsaquo;</div></div>
    </div>
    <div class="svc">
      <div class="circle"><svg width="36" height="36" viewBox="0 0 36 36" fill="none" stroke="#fff" stroke-width="3"><path d="M5 5v26h26"/><path d="M10 24l7-8 5 5 8-11"/></svg></div>
      <div><h3>Marketing Strategy</h3><p>Tawny Reef will help you define the best overall strategy for your business, to help focus all of your marketing.</p><div class="read">Read More &rsaquo;</div></div>
    </div>
  </div>
</section>

<section class="plans">
  <h2 class="head">Our Plans</h2>
  <p class="lead">Check our plans. We're very reasonable when it comes about pricing</p>
  <div class="plan-grid">
    <div class="plan">
      <div class="badge"><svg width="54" height="54" viewBox="0 0 54 54" fill="#c5323a"><path d="M15 6h24v14c0 7-5 12-12 12s-12-5-12-12z"/><path d="M15 10H7c0 8 4 12 9 12M39 10h8c0 8-4 12-9 12" fill="none" stroke="#c5323a" stroke-width="3"/><rect x="24" y="31" width="6" height="8"/><rect x="16" y="39" width="22" height="7"/></svg></div>
      <h3>Reputation Management</h3>
      <ul>
        <li>Access to Ratekit Review platform for</li>
        <li>generating reviews</li>
        <li>Review monitoring</li>
        <li>Local directory listing monitoring</li>
        <li>&amp; correction</li>
      </ul>
    </div>
    <div class="plan">
      <div class="badge"><svg width="56" height="56" viewBox="0 0 36 36" fill="#c5323a"><path d="M4 14h7l14-8v24l-14-8H4z"/><path d="M9 22l3 8h4l-3-8z"/><path d="M29 12l4-3M29 18h5M29 24l4 3" stroke="#c5323a" stroke-width="2"/></svg></div>
      <h3>Social Media Updates + SERM</h3>
      <ul>
        <li>Regular Friendhub/other social updates</li>
        <li>and/or blog posts</li>
        <li>Includes all of our Reputation</li>
        <li>Management services</li>
      </ul>
    </div>
    <div class="plan">
      <div class="badge"><svg width="52" height="52" viewBox="0 0 36 36" fill="none" stroke="#c5323a" stroke-width="3"><path d="M5 5v26h26"/><path d="M10 24l7-8 5 5 8-11"/></svg></div>
      <h3>Comprehensive Marketing Strategy</h3>
      <ul>
        <li>Marketing strategy for your business</li>
        <li>both online &amp; off</li>
        <li>Reputation Management</li>
        <li>Social Media Updates</li>
      </ul>
    </div>
  </div>
</section>

<section class="audit">
  <h2 class="head">SEO Site Audit</h2>
  <p>Find out how your website stacks up before your customers do. Run a free audit to see your search visibility, page speed, broken links and local listing accuracy, then get a clear list of fixes ranked by impact so you know exactly where to start first.</p>
  <div class="audit-widget"><div class="sq"></div><span>Dunefold.example</span></div>
</section>

<section class="contact">
  <h2 class="head">Ready to win the internet?</h2>
  <p class="lead">Get in touch. We're happy to answer any questions you have, and ready to start developing your custom digital marketing strategy to win the internet for your business.</p>
  <div class="form">
    <div class="field">Name :</div>
    <div class="field">Email :</div>
    <div class="field">Phone :</div>
    <div class="submit">Submit</div>
  </div>
  <div class="message">Message :</div>
  <div class="info">
    <div class="info-top">
      <div class="info-dot"></div>
      <p>Saltmeadow Digital Agency<br>48 Larkspur Row, 12th Floor<br>Brookhaven<br>United States</p>
    </div>
    <div class="info-line"><svg width="16" height="16" viewBox="0 0 16 16" fill="#fff"><path d="M3 1l3 1 1 3-2 2c1 2 2 3 4 4l2-2 3 1 1 3-2 2C7 15 1 9 1 3z"/></svg>Phone : 0555 0148 2290</div>
    <div class="info-line"><svg width="16" height="13" viewBox="0 0 16 13" fill="none" stroke="#fff" stroke-width="1.5"><rect x="1" y="1" width="14" height="11"/><path d="M1 1l7 6 7-6"/></svg>Email : hello@saltmeadowdigital.example</div>
  </div>
</section>

<footer class="footer">
  <div>Copyright &copy; 2016. Tawny Reef Advisory. All Rights Reserved.</div>
  <div class="social">Connect with our social network : <i></i><i></i><i></i></div>
</footer>

</body>
</html>
```